US company marketing to law enforcement needs brochure design

We have created a new logo and now need to update our printed material. What we really need is a "style" or "template" for how our brochures will look in the future. Enclosed is the brochure draft with the old style and logo. Also enclosed is the new logo. As we are marketing to US law enforcement it is important the the brochure design is strong, powerful and that we are looking experienced and trustworthy. However, we also want to look modern in line with the logo update.

Target Market(s)

Law enforcement

Industry/Entity Type

Marketing

```html
<!DOCTYPE html>
<html lang="en">
<head>
<meta charset="utf-8">
<title>Steadfast Justice Brochure Template</title>
<link rel="stylesheet" href="https://fonts.googleapis.com/css2?family=Open+Sans:wght@400;600&family=Roboto+Condensed:ital,wght@0,300;0,400;0,700;1,700&display=swap">
<style>
:root{
  --navy:#213a6e;
  --backdrop:#8c8c8c;
  --paper:#ffffff;
  --panel-grey:#e3e4e6;
  --faint:#eeeff1;
  --ink:#222;
  --body-grey:#4d4d4d;
  --rule:#b9c0cf;
  --accent-yellow:#f2d43a;
}
*{margin:0;padding:0;box-sizing:border-box}
html,body{width:900px;height:1200px;overflow:hidden;background:var(--backdrop)}
body{position:relative;font-family:"Roboto Condensed",Arial,sans-serif;color:var(--ink)}
.page{position:absolute;background:var(--paper);box-shadow:2px 3px 6px rgba(0,0,0,.35);overflow:hidden}

/* Brand lockup */
.brand{position:absolute;display:flex;align-items:center;gap:8px;font-family:"Open Sans",Arial,sans-serif;font-weight:600;white-space:nowrap}
.brand-dot{border-radius:50%;background:var(--navy);flex:none}
.tagline{font-family:"Roboto Condensed",Arial,sans-serif;font-style:italic;font-weight:700;color:var(--navy);white-space:nowrap}

/* Back cover */
.back-cover{left:57px;top:28px;width:383px;height:542px}
.back-cover svg{position:absolute;left:0;top:0}
.back-cover .brand{left:18px;top:477px;font-size:17px;color:#7a7f88}
.back-cover .brand-dot{width:32px;height:32px}
.back-cover .tagline{position:absolute;left:12px;top:513px;width:220px;font-size:9px;border-top:1px solid var(--rule);padding-top:3px}

/* Front cover */
.front-cover{left:450px;top:28px;width:378px;height:540px;background:var(--navy)}
.front-cover .cover-mark{position:absolute;left:8px;top:7px;width:100px;height:100px;border-radius:50%;background:var(--paper)}
.front-cover .cover-photo{position:absolute;left:150px;top:0;width:228px;height:540px;background:linear-gradient(160deg,#e9eef3 0%,#8d9aa7 35%,#4a5562 60%,#c9d2da 100%)}
.cover-title{position:absolute;left:8px;top:286px;width:132px;font-weight:300;font-size:20px;line-height:24px;color:#e6ebf4;border-bottom:1px solid #7287b0;padding-bottom:6px}
.program-list{position:absolute;left:10px;top:372px;list-style:none;font-weight:700;font-size:12.5px;line-height:18.7px;color:#fff}
.front-cover .rule{position:absolute;left:8px;top:472px;width:132px;border-top:1px solid #7287b0}
.front-cover .brand{left:10px;top:490px;font-size:11px;color:#fff}
.front-cover .brand-dot{width:20px;height:20px;background:#fff}

/* Inner spread */
.spread{left:28px;top:583px;width:838px;height:595px}
.spread-header{position:absolute;left:0;top:0;width:838px;height:42px}
.spread-header .brand{left:12px;top:12px;font-size:11px;color:#7a7f88}
.spread-header .brand-dot{width:20px;height:20px}
.spread-header .tagline{position:absolute;right:12px;top:20px;font-size:9.2px}

.programs-panel{position:absolute;left:0;top:42px;width:419px;height:387px;background:var(--panel-grey)}
.programs-title{position:absolute;left:0;width:419px;top:10px;text-align:center;font-weight:400;font-size:23px;line-height:28px;color:var(--navy)}
.programs-sub{position:absolute;left:0;width:419px;top:38px;text-align:center;font-size:11.5px;line-height:14px;font-weight:400;color:var(--ink);white-space:nowrap}
.programs-chart{position:absolute;left:26px;top:61px;width:366px;height:312px;background:var(--paper)}
.programs-chart svg{position:absolute;left:0;top:0}
.stage-label{position:absolute;font-weight:700;font-size:8.2px;line-height:10px;color:var(--navy);white-space:nowrap}

.flex-photo{position:absolute;left:0;top:442px;width:150px;height:124px;background:linear-gradient(120deg,#4b4f57,#8a8f96 55%,#2c2f35)}
.flex-title{position:absolute;left:157px;top:476px;font-weight:400;font-size:24px;line-height:24px;color:var(--ink);white-space:nowrap}
.flex-title strong{color:var(--navy);font-weight:700;display:block}
.flex-text{position:absolute;left:157px;top:533px;width:250px;font-weight:300;font-size:12px;line-height:14px;color:var(--body-grey)}

.gavel-photo{position:absolute;left:428px;top:47px;width:213px;height:258px;background:linear-gradient(170deg,#f2f3f5 0%,#b9bec4 40%,#3c3f44 70%,#9ea3a9 100%)}
.benefit{position:absolute;width:100px;font-weight:300;font-size:8.6px;line-height:10.6px;color:var(--body-grey)}
.benefit h3{font-size:9px;line-height:11.4px;color:var(--ink);font-weight:700}

.task-panel{position:absolute;left:640px;top:42px;width:198px;height:553px}
.task-panel svg{position:absolute;left:0;top:0}
.task-list{position:absolute;left:56px;top:21px;width:134px}
.task{height:96px;font-weight:300;font-size:8.5px;line-height:12px;color:#eef1f7}
.task h3{font-size:8.6px;font-weight:400;color:var(--accent-yellow);line-height:12px}
</style>
</head>
<body>

<section class="page back-cover">
  <svg width="383" height="542" viewBox="0 0 383 542">
    <circle cx="190" cy="300" r="180" fill="var(--faint)"/>
    <polygon points="305,0 383,0 383,542 303,542 152,288" fill="var(--navy)"/>
    <polyline points="305,0 152,288 303,542" fill="none" stroke="#c9cdd4" stroke-width="4"/>
    <circle cx="173" cy="288" r="11" fill="var(--paper)"/>
  </svg>
  <div class="brand"><span class="brand-dot"></span>Steadfast Justice</div>
  <p class="tagline">The Nation's Trusted Administrator of offender Programs</p>
</section>

<section class="page front-cover">
  <div class="cover-mark"></div>
  <div class="cover-photo" role="img" aria-label="Close-up photograph of a wooden judge's gavel with a pair of handcuffs"></div>
  <h1 class="cover-title">Comprehensive Offender Programs</h1>
  <ul class="program-list">
    <li>Pre-trial</li><li>Diversion</li><li>Deferred Prosecution</li><li>Jail Alternative</li><li>Probation</li>
  </ul>
  <div class="rule"></div>
  <div class="brand"><span class="brand-dot"></span>Steadfast Justice</div>
</section>

<section class="page spread">
  <header class="spread-header">
    <div class="brand"><span class="brand-dot"></span>Steadfast Justice</div>
    <p class="tagline">The Nation's Trusted Administrator of Offender Programs</p>
  </header>

  <div class="programs-panel">
    <h2 class="programs-title">Comprehensive Offender Programs</h2>
    <p class="programs-sub">We administer Offender Programs at every stage of the criminal justice process</p>
    <div class="programs-chart">
      <svg width="366" height="312" viewBox="0 0 366 312">
        <g fill="none" stroke-width="7">
          <path d="M96.1 13.5 A125 125 0 0 1 163.8 26.6" stroke="#f2d43a"/>
          <path d="M163.8 26.6 A125 125 0 0 1 213 71.8" stroke="#e0282c"/>
          <path d="M213 71.8 A125 125 0 0 1 232 138" stroke="#8e3a96"/>
          <path d="M232 138 A125 125 0 0 1 213 204.2" stroke="#2f6db5"/>
          <path d="M213 204.2 A125 125 0 0 1 163.8 249.4" stroke="#1aa3a0"/>
          <path d="M163.8 249.4 A125 125 0 0 1 96.1 262.5" stroke="#c8d92b"/>
        </g>
        <circle cx="107" cy="138" r="78" fill="var(--navy)"/>
        <g stroke="#9aa0a8" stroke-width="1">
          <line x1="175" y1="33" x2="217" y2="26"/>
          <line x1="219" y1="83" x2="252" y2="79"/>
          <line x1="232" y1="145" x2="265" y2="149"/>
          <line x1="213" y1="204" x2="247" y2="210"/>
          <line x1="164" y1="249" x2="219" y2="265"/>
        </g>
        <g fill="#fff" stroke="#222" stroke-width="1">
          <circle cx="175" cy="33" r="3"/><circle cx="219" cy="83" r="3"/><circle cx="232" cy="145" r="3"/><circle cx="213" cy="204" r="3"/><circle cx="164" cy="249" r="3"/>
        </g>
        <g stroke="#fff" stroke-width="2">
          <circle cx="238" cy="26" r="21" fill="#3b3f5c" role="img" aria-label="Photo of a police officer"/>
          <circle cx="273" cy="79" r="21" fill="#cfd2d6" role="img" aria-label="Photo of handcuffs"/>
          <circle cx="286" cy="149" r="21" fill="#7e93ad" role="img" aria-label="Photo of scales of justice"/>
          <circle cx="268" cy="212" r="21" fill="#d8641f" role="img" aria-label="Photo of an inmate in orange uniform"/>
          <circle cx="239" cy="272" r="21" fill="#d9a52a" role="img" aria-label="Photo of a probation badge"/>
        </g>
      </svg>
      <span class="stage-label" style="left:265px;top:22px">Pre-Trial</span>
      <span class="stage-label" style="left:300px;top:76px">Diversion</span>
      <span class="stage-label" style="left:313px;top:137px">Deferred<br>Prosecution</span>
      <span class="stage-label" style="left:302px;top:200px">Jail<br>Alternative</span>
      <span class="stage-label" style="left:264px;top:273px">Probation</span>
    </div>
  </div>

  <div class="flex-photo" role="img" aria-label="Photograph of two men in a meeting behind bars"></div>
  <h2 class="flex-title"><strong>Flexible solutions for</strong>your jurisdiction needs</h2>
  <p class="flex-text">Not a onesize fits all solution; Each program developed and administerd to your specifications</p>

  <div class="gavel-photo" role="img" aria-label="Photograph of a gavel resting on a sound block"></div>
  <div class="benefit" style="left:428px;top:312px"><h3>Experienced<br>proffesionals</h3>We have created a new logo and now need to update our printed material. What we really need is a "style" or "template" for how our brochures will look in the future. Enclosed is the brochure draft with the old style and logo. Also enclosed is the new logo</div>
  <div class="benefit" style="left:534px;top:312px">logo update.<h3>Save Resources/<br>Reduced Work load</h3>We have created a new logo and now need to update our printed material. What we really need is a "style" or "template" for how our brochures will look in the future. Enclosed is the brochure draft with the old style and logo. Also enclosed is the new logo</div>
  <div class="benefit" style="left:428px;top:469px"><h3>Control/Transparency</h3>. As we are marketing to US law enforcement it is important the the brochure design is strong, powerful and that we are looking experienced and trustworthy. However, we also want to look modern in line with the</div>
  <div class="benefit" style="left:534px;top:469px"><h3>Technology/Equipment</h3>. As we are marketing to US law enforcement it is important the the brochure design is strong, powerful and that we are looking experienced and trustworthy. However, we also want to look modern in line with the logo update.</div>

  <aside class="task-panel">
    <svg width="198" height="553" viewBox="0 0 198 553">
      <polygon points="28,0 198,0 198,553 28,553 28,295 8,280 28,265" fill="var(--navy)"/>
      <polyline points="28,0 28,265 8,280 28,295 28,553" fill="none" stroke="#c9cdd4" stroke-width="3"/>
      <circle cx="20" cy="280" r="9" fill="var(--paper)"/>
    </svg>
    <div class="task-list">
      <div class="task"><h3>Task Description</h3>We have created a new logo and now need to update our printed material. What we really need is a "style" or "template" for how our brochures will look in the future. Enclosed is the brochure draft with the old style and logo. Also enclosed is the new logo</div>
      <div class="task"><h3>Task Description</h3>. As we are marketing to US law enforcement it is important the the brochure design is strong, powerful and that we are looking experienced and trustworthy. However, we also want to look modern in line with the logo update.</div>
      <div class="task"><h3>Task Description</h3>. As we are marketing to US law enforcement it is important the the brochure design is strong, powerful and that we are looking experienced and trustworthy. However, we also want to look modern in line with the logo update.</div>
      <div class="task"><h3>Task Description</h3>. As we are marketing to US law enforcement it is important the the brochure design is strong, powerful and that we are looking experienced and trustworthy. However, we also want to look modern in line with the logo update.</div>
      <div class="task"><h3>Task Description</h3>. As we are marketing to US law enforcement it is important the the brochure design is strong, powerful and that we are looking experienced and trustworthy. However, we also want to look modern in line with the logo update.</div>
    </div>
  </aside>
</section>

</body>
</html>
```